I need A design for a Flyer to market the Kelvo Dock Solution.
I would like for the flyer to contain all relevant necessary data, such as product description, benefits etc. Not all attached write-up content must be added, but main highlights.

Target Market(s)

Residential Buildings
Commercial Buildings
Banks
Schools
Governmental Buildings
Hospitals
Malls
Hotels
Restaurants

Industry/Entity Type

Parking

Requirements
Must have
• 3-d Image of Kelvo Dock
Product Range Image

```html
<!DOCTYPE html>
<html lang="en">
<head>
<meta charset="utf-8">
<title>Kelvo Dock Solution Flyer</title>
<link rel="stylesheet" href="https://fonts.googleapis.com/css2?family=Roboto+Condensed:wght@400;700&family=Arimo:wght@400;700&display=swap">
<style>
  :root {
    --teal: #0f7f86;
    --teal-deep: #0b6d73;
    --teal-light: #2aa2a6;
    --ink: #111;
    --band: #050505;
    --paper: #fff;
    --grey-text: #444;
    --stage: #e9e9e9;
    --photo-steel: #9aa7ad;
  }
  * { box-sizing: border-box; margin: 0; padding: 0; }
  html, body { width: 1200px; height: 823px; overflow: hidden; }
  body { background: var(--stage); position: relative; font-family: "Arimo", Arial, sans-serif; }

  .flyer { position: absolute; top: 32px; width: 520px; height: 731px; overflow: hidden; box-shadow: 0 2px 8px rgba(0,0,0,.25); }
  .flyer--back { left: 50px; background: var(--paper); }
  .flyer--front { left: 635px; background: linear-gradient(160deg, #1a9398 0%, var(--teal) 55%, var(--teal-deep) 100%); }

  /* back side */
  .back__headline { position: absolute; top: 30px; left: 0; width: 100%; text-align: center; font-family: "Roboto Condensed", sans-serif; font-weight: 700; font-size: 31px; color: var(--teal); letter-spacing: -.2px; }
  .market-band { position: absolute; top: 75px; left: 0; width: 100%; height: 133px; background: var(--band); }
  .market-list { position: absolute; list-style: none; top: 12px; }
  .market-list--a { left: 64px; }
  .market-list--b { left: 314px; top: 10px; }
  .market-list li { display: flex; align-items: center; height: 22.5px; color: #fff; font-weight: 700; font-size: 16.5px; }
  .market-list svg { width: 15px; height: 15px; margin-right: 9px; }

  .photo { position: absolute; }
  .photo--garage { left: 57px; top: 230px; width: 207px; height: 133px; background: linear-gradient(180deg, #c9c6bc 0%, #8f8b80 45%, #5d5e5f 100%); }
  .photo--gate { left: 269px; top: 230px; width: 207px; height: 133px; background: linear-gradient(180deg, #c7d0cf 0%, #a58f6a 40%, #3f5e6a 100%); }

  .info-col { position: absolute; top: 378px; width: 192px; }
  .info-col--desc { left: 59px; }
  .info-col--benefits { left: 279px; }
  .info-col h2 { font-size: 14.5px; font-weight: 700; color: var(--ink); margin-bottom: 9px; }
  .info-col p { font-size: 8.4px; line-height: 10.9px; color: var(--grey-text); }

  .swoosh { position: absolute; left: 100px; top: 545px; width: 320px; height: 12px; background: radial-gradient(ellipse at center, rgba(0,0,0,.35) 0%, rgba(0,0,0,0) 70%); }

  .brand { display: flex; align-items: center; justify-content: center; gap: 10px; font-family: "Roboto Condensed", sans-serif; font-weight: 700; color: #1d1d1b; }
  .brand__dot { width: 16px; height: 16px; border-radius: 50%; background: var(--teal); }
  .back__brand { position: absolute; top: 573px; left: 0; width: 100%; font-size: 34px; letter-spacing: 1px; }

  .contact { position: absolute; left: 20px; width: 480px; font-size: 7.6px; color: #222; }
  .contact__row1 { top: 628px; display: flex; justify-content: space-between; border-bottom: 1.5px solid var(--teal); padding-bottom: 2px; }
  .contact__row1 span { color: var(--teal); }
  .contact__row2 { top: 642px; text-align: right; font-weight: 700; }
  .contact__row3 { top: 655px; font-weight: 700; }
  .contact__row3 .tel { color: var(--teal); margin-left: 14px; }
  .back__rule { position: absolute; left: 20px; top: 680px; width: 480px; height: 1.5px; background: var(--teal); }
  .back__web { position: absolute; top: 697px; width: 100%; text-align: center; font-size: 18px; color: var(--teal); }

  /* front side */
  .photo--racks { position: absolute; right: 0; top: 0; width: 350px; height: 571px;
    background: linear-gradient(90deg, rgba(15,127,134,1) 0%, rgba(15,127,134,0) 22%), linear-gradient(180deg, #b9c6cb 0%, var(--photo-steel) 40%, #6f7a7e 75%, #c7bfb1 100%); }
  .front__headline { position: absolute; left: 50px; top: 80px; font-family: "Roboto Condensed", sans-serif; font-weight: 700; font-size: 49px; line-height: 55px; color: #fff; }
  .photo--sign { position: absolute; left: 41px; top: 367px; width: 144px; height: 144px; border-radius: 50%; border: 5px solid #fff; box-shadow: 0 3px 8px rgba(0,0,0,.3); background: linear-gradient(135deg, #e9e9e6 0%, #b9b9b4 45%, #b3262b 60%, #6a6d70 100%); }
  .front__band { position: absolute; left: 0; top: 571px; width: 100%; height: 108px; background: var(--paper); }
  .front__brand { position: absolute; top: 34px; left: 0; width: 100%; font-size: 36px; letter-spacing: 1px; }
  .front__tel { position: absolute; top: 699px; width: 100%; text-align: center; color: #fff; font-size: 19.5px; letter-spacing: .3px; }
</style>
</head>
<body>

<section class="flyer flyer--back">
  <h1 class="back__headline">We provide complete parking solution</h1>

  <div class="market-band">
    <ul class="market-list market-list--a">
      <li><svg viewBox="0 0 16 16"><path d="M2 2L14 14M14 2L2 14M8 1V15M1 8H15" stroke="#fff" stroke-width="1.4"/></svg>Residential Buildings</li>
      <li><svg viewBox="0 0 16 16"><path d="M2 2L14 14M14 2L2 14M8 1V15M1 8H15" stroke="#fff" stroke-width="1.4"/></svg>Commercial Buildings</li>
      <li><svg viewBox="0 0 16 16"><path d="M2 2L14 14M14 2L2 14M8 1V15M1 8H15" stroke="#fff" stroke-width="1.4"/></svg>Banks</li>
      <li><svg viewBox="0 0 16 16"><path d="M2 2L14 14M14 2L2 14M8 1V15M1 8H15" stroke="#fff" stroke-width="1.4"/></svg>Schools</li>
      <li><svg viewBox="0 0 16 16"><path d="M2 2L14 14M14 2L2 14M8 1V15M1 8H15" stroke="#fff" stroke-width="1.4"/></svg>Governmental Buildings</li>
    </ul>
    <ul class="market-list market-list--b">
      <li><svg viewBox="0 0 16 16"><path d="M2 2L14 14M14 2L2 14M8 1V15M1 8H15" stroke="#fff" stroke-width="1.4"/></svg>Hospitals</li>
      <li><svg viewBox="0 0 16 16"><path d="M2 2L14 14M14 2L2 14M8 1V15M1 8H15" stroke="#fff" stroke-width="1.4"/></svg>Malls</li>
      <li><svg viewBox="0 0 16 16"><path d="M2 2L14 14M14 2L2 14M8 1V15M1 8H15" stroke="#fff" stroke-width="1.4"/></svg>Hotels</li>
      <li><svg viewBox="0 0 16 16"><path d="M2 2L14 14M14 2L2 14M8 1V15M1 8H15" stroke="#fff" stroke-width="1.4"/></svg>Restaurants</li>
    </ul>
  </div>

  <div class="photo photo--garage" role="img" aria-label="Photo of an underground parking garage with parked cars and yellow pillars"></div>
  <div class="photo photo--gate" role="img" aria-label="Photo of a parking entrance with barrier gates and cars driving in"></div>

  <div class="info-col info-col--desc">
    <h2>PRODUCT DESCRIPTION</h2>
    <p>Lorem ipsum dolor sit amet, consectetuer adipiscing elit, sed diam nonummy nibh euismod tincidunt ut laoreet dolore magna aliquam erat volutpat. Ut wisi enimLorem ipsum dolor sit amet, consectetuer adipiscing elit, sed diam nonummy nibh euismod tincidunt ut laoreet dolore magna aliquam erat volutpat. Ut wisi enimLorem ipsum dolor sit amet, consectetuer adipiscing elit, sed diam nonummy nibh euismod tincidunt ut laoreet dolore magna aliquam erat volutpat. Ut wisi enim</p>
  </div>
  <div class="info-col info-col--benefits">
    <h2>BENEFITS</h2>
    <p>Lorem ipsum dolor sit amet, consectetuer adipiscing elit, sed diam nonummy nibh euismod tincidunt ut laoreet dolore magna aliquam erat volutpat. Ut wisi enimLorem ipsum dolor sit amet, consectetuer adipiscing elit, sed diam nonummy nibh euismod tincidunt ut laoreet dolore magna aliquam erat volutpat. Ut wisi enimLorem ipsum dolor sit amet, consectetuer adipiscing elit, sed diam nonummy nibh euismod tincidunt ut laoreet dolore magna aliquam erat volutpat. Ut wisi enim</p>
  </div>

  <div class="swoosh"></div>
  <div class="brand back__brand"><span class="brand__dot"></span>NORVANE CONSTRUCTION</div>

  <div class="contact contact__row1"><p>E mail: <span>info@norvanecon.net</span></p><span>www.norvanecon.net</span></div>
  <p class="contact contact__row2">18 Harbor St, Meridian Tower, Zone 3, Port City – Tel 5550142 – Fax 5550143</p>
  <p class="contact contact__row3">18 Harbor St. Meridian Tower, Zone 3, 2nd Floor, Port City &nbsp; P.O.Box 1120, Bayside, 40021 <span class="tel">Tel: +(000) 5550142 &nbsp; Fax : +(000) 5550143</span></p>
  <div class="back__rule"></div>
  <p class="back__web">www.norvanecon.net</p>
</section>

<section class="flyer flyer--front">
  <div class="photo--racks" role="img" aria-label="Photo of a multi-level automated parking rack holding stacked cars"></div>
  <h1 class="front__headline">Kelvo<br>Automated<br>Dock<br>Solution</h1>
  <div class="photo--sign" role="img" aria-label="Round photo of a 24 hour parking ticket machine sign"></div>
  <div class="front__band">
    <div class="brand front__brand"><span class="brand__dot"></span>NORVANE CONSTRUCTION</div>
  </div>
  <p class="front__tel">Tel: +(000) 5550142</p>
</section>

</body>
</html>
```